Brightwell Wiring Needs A Logo Design

We need a logo for my new company based out of Sacramento, Ca called Brightwell Wiring. The name says it all, my electrical contracting business provides "Brightwell Craftsman Work" I'm open to any colors that pop and customers to say Wow. I would love to print my cards on metal.

Contact Information for Business Card

The card needs to have as follows
Name of company: Brightwell Wiring
My Name: Marco Delvane
Phone # 916-555-0147
CL# 4873920
Email: brightwellwiring@mailtorva.com
and a slogan that represent "BRIGHTWELL"

Requirements
Must have
• The card needs to have as follows
• Name of company: Brightwell Wiring
• My Name : Marco Delvane
• Phone # 916-555-0147
• CL# 4873920
• Email: brightwellwiring@mailtorva.com
• and a slogan that represent "BRIGHTWELL"
Nice to have
• popping colors
• electrical Arcing

```html
<!DOCTYPE html>
<html lang="en">
<head>
<meta charset="utf-8">
<title>Brightwell Wiring — Business Card</title>
<link href="https://fonts.googleapis.com/css2?family=Open+Sans:wght@400;600;700&display=swap" rel="stylesheet">
<style>
  :root {
    --page: #4a4a4a;
    --card: #000000;
    --lime: #b7dc3a;
    --lime-soft: #d6ef8a;
    --white: #ffffff;
    --grey: #9a9a9a;
    --cyan: #12a9c4;
    --arc-core: #c9c6ff;
    --arc-glow: #5a4fd8;
  }
  * { margin: 0; padding: 0; box-sizing: border-box; }
  html, body {
    width: 1200px; height: 1000px; overflow: hidden;
    background: var(--page);
    font-family: "Open Sans", sans-serif;
  }
  .card {
    position: absolute; left: 107px; top: 229px;
    width: 986px; height: 542px;
    background: var(--card);
    border-radius: 20px;
    overflow: hidden;
  }
  .card__arcing {
    position: absolute; left: 0; top: 0;
    width: 986px; height: 542px;
  }
  .card__title {
    position: absolute; left: 30px; top: 68px;
    font-size: 50px; font-weight: 600; letter-spacing: 0.5px;
    background: linear-gradient(90deg, var(--white) 0%, var(--lime-soft) 45%, var(--lime) 100%);
    -webkit-background-clip: text; background-clip: text;
    color: transparent;
  }
  .card__name-tab {
    position: absolute; left: 0; top: 293px;
    width: 32px; height: 36px;
    background: var(--white);
    border-radius: 0 18px 18px 0;
    display: flex; align-items: center; justify-content: center;
  }
  .card__name {
    position: absolute; left: 69px; top: 290px;
    font-size: 35px; color: var(--lime);
  }
  .contact {
    position: absolute; left: 34px; top: 358px;
    list-style: none;
  }
  .contact__item {
    display: flex; align-items: center; gap: 12px;
    height: 44px;
    font-size: 25px; color: var(--lime);
  }
  .contact__item svg { width: 22px; height: 22px; }
  .card__licence {
    position: absolute; left: 22px; top: 494px;
    font-size: 24px; color: var(--lime);
  }
  .brand {
    position: absolute; left: 690px; top: 330px;
    width: 270px;
    display: flex; flex-direction: column; align-items: center;
    text-align: center;
  }
  .brand__square { width: 60px; height: 60px; background: var(--cyan); margin-bottom: 10px; }
  .brand__name {
    font-size: 30px; font-weight: 700; color: var(--white);
    line-height: 1.05; letter-spacing: 1px;
  }
  .brand__slogan {
    margin-top: 8px;
    font-size: 15px; font-weight: 400; color: var(--grey);
    letter-spacing: 1.5px; text-transform: uppercase;
  }
</style>
</head>
<body>
  <div class="card">
    <svg class="card__arcing" role="img" aria-label="Electrical arcing lightning bolts streaking diagonally across the card" viewBox="0 0 986 542">
      <defs>
        <radialGradient id="arcGlow" cx="50%" cy="50%" r="50%">
          <stop offset="0%" stop-color="#c9c6ff" stop-opacity="0.55"/>
          <stop offset="45%" stop-color="#5a4fd8" stop-opacity="0.3"/>
          <stop offset="100%" stop-color="#5a4fd8" stop-opacity="0"/>
        </radialGradient>
      </defs>
      <ellipse cx="700" cy="210" rx="420" ry="110" transform="rotate(-28 700 210)" fill="url(#arcGlow)"/>
      <ellipse cx="380" cy="480" rx="90" ry="40" transform="rotate(-50 380 480)" fill="url(#arcGlow)" opacity="0.6"/>
    </svg>

    <h1 class="card__title">BRIGHTWELL WIRING</h1>

    <div class="card__name-tab">
      <svg width="20" height="20" viewBox="0 0 20 20"><circle cx="10" cy="6" r="4.5" fill="#8cc63f"/><path d="M2 19c0-5 3.5-7.5 8-7.5s8 2.5 8 7.5z" fill="#8cc63f"/></svg>
    </div>
    <p class="card__name">Marco Delvane</p>

    <ul class="contact">
      <li class="contact__item">
        <svg viewBox="0 0 22 22" fill="none" stroke="currentColor" stroke-width="1.6"><circle cx="11" cy="11" r="9.5"/><path d="M7.5 6.5c0 4.5 3.5 8.5 8 8.5l1-2-2.5-1.2-1 1c-1.5-.7-2.8-2-3.5-3.5l1-1L9.3 5.8z"/></svg>
        916-555-0147
      </li>
      <li class="contact__item">
        <svg viewBox="0 0 22 22" fill="none" stroke="currentColor" stroke-width="1.6"><rect x="2" y="5" width="18" height="12"/><path d="M2 5l9 7 9-7"/></svg>
        brightwellwiring@mailtorva.com
      </li>
      <li class="contact__item">
        <svg viewBox="0 0 22 22" fill="none" stroke="currentColor" stroke-width="1.6"><circle cx="11" cy="11" r="9.5"/><ellipse cx="11" cy="11" rx="4" ry="9.5"/><path d="M1.5 11h19M3 6h16M3 16h16"/></svg>
        www.brightwellwiring.net
      </li>
    </ul>

    <p class="card__licence">CL# 4873920</p>

    <div class="brand">
      <span class="brand__square"></span>
      <span class="brand__name">BRIGHTWELL<br>WIRING</span>
      <span class="brand__slogan">Brightwell Craftsman Work</span>
    </div>
  </div>
</body>
</html>
```